4 x 9 Rack Card Design: Cheer Each Game Advertising Campaign

We would like a 4 x 9 Rack Card Designed using our logo as the basis for the design. We would like to incorporate the images of the shoes & the colors that are on our logo. We are attaching an image of the logo for your use.

The design should use both the front & back of the 4 x 9 card.

All text & fonts should be in "comic sans".

The card should have a fun, youthful, cartoon feel to it.

We would like the following information on the card:

Our Tag Line: Charity providing Athletic Footwear to Kids

Our Catch Phrase: "Cheer Each Game". Please include small images of various sports balls under, or around or near the catch phrase. Please use images of a Basketball, baseball, golf ball, soccer ball, Hockey Puck, American Football, Tennis ball.

Our Contact Information: PO Box 57392, Phoenix, AZ 85077; phone 480.312.4456; www.hop-and-laces.org; also use the "find us on chatterbook" image.

Who we are: We are a 501(c)3 non-profit organization providing athletic footwear to disadvantaged and at-risk youth. The proper footwear allows participation in sports activities providing a healthy outlet for energy, increased self confidence, reduced juvenile crime rates, decline in alcohol, tobacco and drug dependency, strengthened relationships and enhanced academic performance.

A Recipe: We are working on a recipe to be included. In the meantime, we are asking for designs that include a small area for a recipe on the back of the card. The recipe will be easy, with very few ingredients & instructions, so it won't take up too much space on the rack card.

Target Market(s)

Sponsors, endorsers, donators, sports teams.

Industry/Entity Type

Non-Profit

Font styles to use
Other font styles liked:
• Comic Sans

Requirements
Must have
• See project descripion
Nice to have
• See project description. Also, please take a look at our website at www.hop-and-laces.com for our style & additional information about our organization.

```html
<!DOCTYPE html>
<html lang="en">
<head>
<meta charset="utf-8">
<title>Hop-and-Laces Rack Card</title>
<link rel="stylesheet" href="https://fonts.googleapis.com/css2?family=Nunito:wght@800;900&family=Arimo:wght@400;700&display=swap">
<style>
  :root {
    --navy: #1b2d7c;
    --red: #e3231f;
    --yellow: #f7ea1c;
    --sun: #f4e600;
    --leaf: #6fc24b;
    --mint: #8fe35f;
    --sea: #2aa59a;
    --ocean: #1f5fb8;
    --band: #16246a;
    --white: #ffffff;
    --brand: #3b72c6;
  }
  * { box-sizing: border-box; margin: 0; padding: 0; }
  html, body { width: 1200px; height: 2700px; overflow: hidden; background: var(--white); }
  .rack-card {
    position: relative;
    width: 1200px;
    height: 2700px;
    overflow: hidden;
    font-family: "Arimo", Arial, sans-serif;
    background: linear-gradient(180deg,
      var(--white) 0px, var(--white) 330px,
      var(--sun) 520px, #d8e51a 1000px,
      var(--leaf) 1450px, var(--sea) 2000px,
      var(--ocean) 2600px);
  }
  .block { position: absolute; left: 0; width: 100%; text-align: center; }

  .brand-name {
    top: 240px;
    font-family: "Nunito", Arial, sans-serif;
    font-weight: 900;
    font-size: 84px;
    color: var(--brand);
    display: flex; justify-content: center; align-items: center; gap: 26px;
  }
  .brand-dot { width: 34px; height: 34px; border-radius: 50%; background: var(--brand); }

  .tagline {
    top: 430px;
    font-family: "Nunito", Arial, sans-serif;
    font-weight: 900;
    font-size: 96px;
    line-height: 94px;
    color: var(--navy);
    -webkit-text-stroke: 10px var(--white);
    paint-order: stroke fill;
  }
  .catch-phrase {
    top: 718px;
    font-family: "Nunito", Arial, sans-serif;
    font-weight: 900;
    font-size: 104px;
    color: var(--red);
    -webkit-text-stroke: 10px var(--white);
    paint-order: stroke fill;
  }
  .sports-balls {
    position: absolute;
    left: 167px; top: 850px;
    width: 866px; height: 165px;
    border-radius: 80px;
    background: linear-gradient(90deg, #c8631f, #f2f2f2 30%, #7a3f1d 55%, #e9f03a 75%, #222 100%);
    opacity: 0.85;
  }
  .mission {
    top: 1080px;
    padding: 0 90px;
    font-weight: 700;
    font-size: 45px;
    line-height: 50px;
    color: var(--yellow);
    text-shadow: 2px 2px 3px rgba(0,0,0,0.35);
  }
  .section-title {
    font-weight: 700;
    font-size: 58px;
    color: var(--mint);
    text-shadow: 2px 2px 3px rgba(0,40,80,0.6);
  }
  .list {
    font-size: 41px;
    line-height: 45.5px;
    color: var(--white);
    text-shadow: 2px 2px 3px rgba(0,0,0,0.35);
    list-style: none;
  }
  .rewards-title { top: 1250px; }
  .rewards-list { top: 1320px; }
  .outcomes-title { top: 1785px; }
  .outcomes-list { top: 1855px; }
  .benefits-title { top: 2250px; }
  .benefits-list { top: 2318px; }

  .closing-note {
    top: 2475px;
    padding: 0 80px;
    font-weight: 700;
    font-size: 30px;
    line-height: 36px;
    color: var(--yellow);
  }
  .contact-band {
    position: absolute; left: 0; bottom: 0;
    width: 100%; height: 96px;
    background: var(--band);
    color: var(--white);
    font-size: 29px; line-height: 36px;
    text-align: center;
    padding-top: 12px;
  }
  .kid-silhouette {
    position: absolute;
    border-radius: 45% 45% 40% 40%;
    background: rgba(255,255,255,0.16);
  }
  .kid-left { left: 20px; top: 1200px; width: 300px; height: 700px; }
  .kid-right { right: 20px; top: 1850px; width: 300px; height: 680px; }
</style>
</head>
<body>
<main class="rack-card">
  <div class="kid-silhouette kid-left" role="img" aria-label="Faint silhouette of a child playing basketball"></div>
  <div class="kid-silhouette kid-right" role="img" aria-label="Faint silhouette of a child swinging a golf club"></div>

  <div class="block brand-name"><span class="brand-dot"></span>Hop-and-Laces</div>

  <h1 class="block tagline">Charity providing<br>Athletic Footwear<br>to Kids</h1>
  <p class="block catch-phrase">"Cheer Each Game"</p>

  <div class="sports-balls" role="img" aria-label="Row of sports balls: basketball, soccer ball, golf ball, football, baseball, tennis ball and hockey puck"></div>

  <p class="block mission">To provide athletic footware to underprivileged and at-risk children and youth, enabling them to participate in sports and other activities.</p>

  <h2 class="block section-title rewards-title">The rewards:</h2>
  <ul class="block list rewards-list">
    <li>Provide a positive outlet for energy</li>
    <li>Create a sense of accomplishment</li>
    <li>Teach leadership &amp; multitasking skills</li>
    <li>Improve memory and problem-solving skills</li>
    <li>Teach teamwork, cooperation &amp; respect</li>
    <li>Foster Self-Discipline</li>
    <li>Encourage goal setting &amp; healthy habits</li>
    <li>Improved family communication and values</li>
    <li>Strengthen peer social interaction and connections</li>
  </ul>

  <h2 class="block section-title outcomes-title">Proven measurable outcomes:</h2>
  <ul class="block list outcomes-list">
    <li>Enhanced academic performance</li>
    <li>Reduced juvenile crime rates</li>
    <li>Improved self esteem</li>
    <li>Decline in tobacco, alcohol &amp; drug use</li>
    <li>Decreased anger &amp; stress</li>
    <li>Decrease in obesity</li>
    <li>Lower teen pregnancy rates</li>
    <li>Higher high school graduation rates</li>
  </ul>

  <h2 class="block section-title benefits-title">Who benefits?</h2>
  <ul class="block list benefits-list">
    <li>Everyone! Children,</li>
    <li>Families, Communities, Employers,</li>
    <li>Schools</li>
  </ul>

  <p class="block closing-note">The proper athletic footware will create a difference in a child's future: Physically, emotionally &amp; economically.</p>

  <footer class="contact-band">
    Our Contact Information: PO Box 57392, Phoenix, AZ 85077; phone<br>
    480.312.4456; www.hop-and-laces.org; also use the "find us on chatterbook" image.
  </footer>
</main>
</body>
</html>
```